Business card design needed for rebranded top-end landscaping business

We need a new business card design, incorporating our logo (colours Green #8dc63f and Grey #8a8c8e) and also some options that include the colour dark navy (eg #000040) as our uniforms are navy with white and grey trim.

We are an innovative landscaping company that maintains high-end gardens for meticulous clients. We pride ourselves on our customer service, our professionalism, and our workmanship.

Our business name needs to be easily read and our branding needs to be bold and memorable, without screaming "tradesman"! We prefer clean lines over lots of fine detail.

The design MUST include:
- Business name ("Brambleton Gardenworks")
- Logo (file uploaded)
- Employee name
- Phone number
- Email address
- www.brambletongardenworks.com.au
- Facepage & Photostream logos
- The Turfcraft Guild logo (file uploaded) along with the word "Member"
- Licence "Lic. 618392K"

OPTIONAL inclusions:
- "Creating outdoor spaces for our community to be inspired, refreshed and re-energised"
- "Landscape Maintenance - Irrigation - Arboriculture" (dashes can be replaced with dots or other)
- "Fully qualified, licensed & insured"
- "Residential - Strata - Commercial - Real Estate" (dashes can be replaced with dots or other)

High-end professionals and retirees, real estate agents

Landscaping

See Project description

Sans Serif

Designer to choose colors to be used in the design.

• Must incorporate our logo, and colours Green #8dc63f and Grey #8a8c8e) from the logo, and the colour DARK NAVY (eg #000040).
• The design MUST include:
• - Business name ("Brambleton Gardenworks")
• - Logo (file uploaded)
• - Employee name
• - Phone number
• - Email address
• - www.brambletongardenworks.com.au
• - Facepage & Photostream logos
• - The Turfcraft Guild logo (file uploaded) along with the word "Member"
• - Licence "Lic. 618392K"
• OPTIONAL inclusions:
• - "Creating outdoor spaces for our community to be inspired, refreshed and re-energised"
• - "Landscape Maintenance - Irrigation - Arboriculture" (dashes can be replaced with dots or other)
• - "Fully qualified, licensed & insured"
• - "Residential - Strata - Commercial - Real Estate" (dashes can be replaced with dots or other)

```html
<!DOCTYPE html>
<html lang="en">
<head>
<meta charset="utf-8">
<title>Brambleton Gardenworks – Business Card</title>
<link rel="stylesheet" href="https://fonts.googleapis.com/css2?family=Montserrat:wght@400&family=Source+Sans+3:ital,wght@0,400;0,600;1,400&display=swap">
<style>
  :root {
    --backdrop: #222629;
    --green: #8dc63f;
    --green-deep: #76a83a;
    --grey: #8a8c8e;
    --grey-text: #6f7173;
    --band-grey: #7d7f82;
    --white: #ffffff;
    --card-light: #ffffff;
    --card-shade: #d3d3d4;
  }
  * { box-sizing: border-box; margin: 0; padding: 0; }
  html, body { width: 1200px; height: 1176px; overflow: hidden; }
  body {
    background: var(--backdrop);
    font-family: "Source Sans 3", Arial, sans-serif;
    position: relative;
  }
  .card {
    position: absolute;
    left: 280px;
    width: 617px;
    height: 352px;
    border-radius: 16px;
    overflow: hidden;
  }
  /* Front */
  .card-front {
    top: 190px;
    background: linear-gradient(200deg, var(--card-light) 25%, var(--card-shade) 100%);
  }
  .holder-name {
    position: absolute; left: 34px; top: 36px;
    font-family: "Montserrat", Arial, sans-serif;
    font-size: 28px; color: var(--grey-text); letter-spacing: 0.5px;
  }
  .holder-title {
    position: absolute; left: 34px; top: 72px;
    font-size: 17px; color: var(--green); letter-spacing: 0.5px;
  }
  .contact-list { list-style: none; position: absolute; left: 34px; top: 163px; }
  .contact-list li {
    display: flex; align-items: center; gap: 10px;
    height: 26px; font-size: 14.5px; color: var(--grey-text);
  }
  .contact-list li.social-first { margin-top: 9px; }
  .contact-list svg { width: 13px; height: 13px; flex: none; }
  .brand-mark {
    position: absolute; left: 394px; top: 40px; width: 200px;
    text-align: center;
  }
  .brand-mark .dot {
    width: 64px; height: 64px; border-radius: 50%;
    background: var(--green); margin: 0 auto 8px;
  }
  .brand-mark .brand-name {
    font-size: 21px; font-weight: 600; color: var(--grey); line-height: 1.1;
  }
  .member-badge {
    position: absolute; left: 485px; top: 170px; width: 112px; text-align: center;
  }
  .member-badge .badge-shape {
    width: 18px; height: 18px; background: var(--green); margin: 0 auto 4px;
  }
  .member-badge span { font-size: 10px; color: #333; letter-spacing: 1px; }
  .bands { position: absolute; left: 0; top: 0; width: 617px; height: 352px; }
  .tagline {
    position: absolute; left: 8px; width: 340px; top: 316px;
    text-align: center; font-size: 13.5px; line-height: 15px; color: var(--white);
  }
  .tagline em { color: var(--green); }
  .credentials {
    position: absolute; left: 360px; width: 250px; top: 304px;
    text-align: center; font-size: 14.5px; line-height: 18px; color: var(--white);
  }
  /* Back */
  .card-back {
    top: 591px; height: 351px;
    background: linear-gradient(135deg, var(--green-deep) 0%, var(--green) 100%);
    text-align: center; color: var(--white);
  }
  .card-back .dot {
    position: absolute; left: 254px; top: 68px;
    width: 110px; height: 110px; border-radius: 50%; background: var(--grey);
  }
  .card-back .brand-name {
    position: absolute; left: 0; right: 0; top: 192px;
    font-size: 40px; font-weight: 600; color: var(--white);
  }
  .service-line {
    position: absolute; left: 0; right: 0;
    font-size: 12px; letter-spacing: 0.3px; word-spacing: 2px;
  }
  .service-line .sep { margin: 0 10px; }
  .services { top: 284px; text-transform: uppercase; }
  .sectors { top: 317px; }
</style>
</head>
<body>

<section class="card card-front">
  <svg class="bands" viewBox="0 0 617 352" aria-hidden="true">
    <polygon points="0,315 357,315 347,352 0,352" fill="var(--band-grey)"/>
    <polygon points="369,300 617,300 617,352 347,352" fill="var(--green)"/>
  </svg>

  <h1 class="holder-name">YOUR NAME</h1>
  <p class="holder-title">JOB TITLE</p>

  <ul class="contact-list">
    <li>
      <svg viewBox="0 0 14 14"><path fill="var(--green)" d="M1 5c0-2 3-3 6-3s6 1 6 3v1H10V5H4v1H1zM3 7h8l1 5H2z"/></svg>
      000 000 0000
    </li>
    <li>
      <svg viewBox="0 0 14 14"><rect x="4" y="1" width="6" height="12" rx="1" fill="none" stroke="var(--green)" stroke-width="1.5"/></svg>
      Email address@brambleton.au
    </li>
    <li>
      <svg viewBox="0 0 14 14"><rect x="1" y="3" width="12" height="8" fill="var(--green)"/><path d="M1 3l6 5 6-5" fill="none" stroke="#fff" stroke-width="1"/></svg>
      www.brambletongardenworks.com.au
    </li>
    <li class="social-first">
      <svg viewBox="0 0 14 14"><rect x="1" y="1" width="12" height="12" rx="2" fill="var(--green)"/></svg>
      /Photostream
    </li>
    <li>
      <svg viewBox="0 0 14 14"><rect x="1" y="1" width="12" height="12" fill="var(--green)"/></svg>
      /Facepage
    </li>
  </ul>

  <div class="brand-mark">
    <div class="dot"></div>
    <p class="brand-name">Brambleton Gardenworks</p>
  </div>

  <div class="member-badge">
    <div class="badge-shape"></div>
    <span>MEMBER</span>
  </div>

  <p class="tagline">Creating outdoor spaces for our community<br>to be <em>inspired, refreshed and re-energised</em></p>
  <p class="credentials">Fully qualified, licensed &amp; insured<br>Lic. 618392K</p>
</section>

<section class="card card-back">
  <div class="dot"></div>
  <p class="brand-name">Brambleton Gardenworks</p>
  <p class="service-line services">Landscape Maintenance<span class="sep">I</span>Irrigation<span class="sep">I</span>Arboriculture</p>
  <p class="service-line sectors">Residential<span class="sep">I</span>Strata<span class="sep">I</span>Commercial<span class="sep">I</span>Real Estate</p>
</section>

</body>
</html>
```